Cover für Erstlingswerk
Ich habe von Ralosa ein phantastisches Cover für mein Buch bekommen. Ganz anders als ich es mir bei Auftragsstellung vorgestellt habe. Sehr innovativ und außergewöhnlich. Die Zusammenarbeit war freundlich und locker, spontan und flexibel. Ich bedanke mich ganz herzlich für dieses wundervolle Cover für mein Herzensprojekt!
Zielgruppe
Es handelt sich um einen Roman, der insbesondere Frauen zwischen 30 und 60 Jahren ansprechen wird.
Aufgabenstellung
Das Cover soll schlicht, ohne Schnörkel sein, bevorzugte Farben blau wie die Nordsee und der Himmel, grün und braun wie der Kiefernwald und das Dünengras und weiß wie die Wolken. Ggf. ein Bezug zu Dänemark. Aber ich bin für alle Ideen offen.
Noch ein Nachtrag: dies ist mein erster Auftrag und mein erstes Buch, daher, wenn es Fragen gibt, bitte stellen. Ich habe auch einen Klappentext, wird der zu diesem Zeitpunkt schon eingebunden? Es steckt viel Herzblut und Zeit in meinem ersten Roman. Wenn ich für das Cover mehr Input geben soll, bitte mitteilen!
Noch ein Nachtrag: Der Titel des Buches lautet "Wo der Wind mich fand" und der Name der Autorin Marla Thorvik.

```html
<!DOCTYPE html>
<html lang="de">
<head>
<meta charset="utf-8">
<title>Wo der Wind mich fand – Marla Thorvik</title>
<link rel="stylesheet" href="https://fonts.googleapis.com/css2?family=Dancing+Script:wght@400;500&family=Overlock:wght@400&family=Alegreya:wght@400&display=swap">
<style>
  :root {
    --sky-top: #2a95d6;
    --sky-mid: #4fb0e6;
    --sky-haze: #b9def3;
    --pine-dark: #1f3a22;
    --pine-mid: #355b32;
    --dune-grass: #c9c4a4;
    --sand: #f3f2ee;
    --sea-light: #bfe0f2;
    --sea: #5cb5e6;
    --title-white: #ffffff;
    --genre-blue: #a9dcf5;
    --author-grey: #4a4a4a;
  }
  * { margin: 0; padding: 0; box-sizing: border-box; }
  html, body {
    width: 768px;
    height: 1200px;
    overflow: hidden;
    background: var(--sand);
  }
  .cover {
    position: relative;
    width: 768px;
    height: 1200px;
    overflow: hidden;
  }
  .cover__scene {
    position: absolute;
    inset: 0;
    background: linear-gradient(
      to bottom,
      var(--sky-top) 0%,
      var(--sky-mid) 35%,
      var(--sky-haze) 55%,
      var(--pine-mid) 56%,
      var(--pine-dark) 66%,
      var(--pine-mid) 73%,
      var(--dune-grass) 76%,
      var(--sand) 80%,
      var(--sand) 88%,
      var(--sea-light) 90%,
      var(--sea) 100%
    );
  }
  .title {
    position: absolute;
    left: 0;
    width: 768px;
    text-align: center;
    font-family: "Dancing Script", cursive;
    font-weight: 400;
    color: var(--title-white);
    line-height: 1;
    white-space: nowrap;
  }
  .title--line1 { top: 50px; font-size: 124px; }
  .title--line2 { top: 196px; font-size: 124px; }
  .title--line3 { top: 330px; font-size: 250px; }
  .genre {
    position: absolute;
    left: 574px;
    top: 348px;
    font-family: "Alegreya", serif;
    font-size: 46px;
    color: var(--genre-blue);
    letter-spacing: 1px;
  }
  .author {
    position: absolute;
    left: 0;
    width: 768px;
    top: 982px;
    text-align: center;
    font-family: "Overlock", sans-serif;
    font-size: 58px;
    color: var(--author-grey);
    letter-spacing: 1px;
  }
</style>
</head>
<body>
  <main class="cover">
    <div class="cover__scene" role="img" aria-label="Foto: blauer Himmel mit Wolken, Kiefernwald mit einem grünen Reetdachhaus hinter Dünengras, weißer Sandstrand und klares Meerwasser im Vordergrund"></div>
    <h1>
      <span class="title title--line1">Wo der</span>
      <span class="title title--line2">Wind mich</span>
      <span class="title title--line3">fand</span>
    </h1>
    <p class="genre">Roman</p>
    <p class="author">Marla Thorvik</p>
  </main>
</body>
</html>
```